Brighter House Storage Scheme Email marketing campaign for Tamsel Energy

Design a visually engaging and professional marketing email to promote the upcoming National Cell Storage Grant to our existing solar clients, encouraging them to install a battery system now to maximise savings. email content example "Subject: ⚡ National Cell Storage Grant is Coming – Maximise Your Solar Savings

Body:
Hi [First Name],

Great news! With the federal election now decided, the National Household Cell Grant Initiative is officially on the way.

While the scheme hasn’t formally launched yet, it's guaranteed—and like the solar rebate before it, the subsidy reduces each year, so the earlier you install, the more you’ll save.

Crucially, the subsidy is only available once per household, so it makes sense to install a system that fully meets your home's battery needs right from the start.

Why add a battery to your existing solar system now?
✅ Store your excess solar energy instead of sending it back to the grid for low feed-in tariffs
✅ Use your stored solar power at night, when electricity prices are highest (typically 5–8pm)
✅ Slash your power bills and avoid rising time-of-use charges
✅ Protect your home from power outages
✅ Increase your self-sufficiency and long-term energy security

If you’ve already installed solar with us, now is the ideal time to complete your setup with a battery system designed to maximise your return—and take full advantage of this one-off federal subsidy.

Call us today or reply to this email to secure your spot and beat the rush.

Let your solar work smarter for your home,
The Tamsel Energy Team"

Target Market(s)

Content: We’ve provided the copy (see attached or below). The key points to emphasise in the design are: The urgency (subsidy winds down each year, limited to one per household). The benefits of installing a battery now, including energy savings, time-of-use charge avoidance, and self-sufficiency. Call to action: “Call us today or reply to this email to secure your spot and beat the rush.”

Industry/Entity Type

Renewable Energy

Colors
0054AA
0677BA
7BADD7
CADEEF
E8F1F8
EB3D1F
EC4F4E
F09395
F8D3D4
FCEDEE

Requirements
Must have
• Clean, modern, and trustworthy – aligned with Tamsel Energy branding. Bold headers and icons to make key points stand out. Include visual elements such as: A solar battery image Infographic or icon-style section showing key battery benefits (e.g. bill savings, backup power, self-consumption) Highlighted call-to-action button (“Secure My Battery Now” or “Beat the Rush”)
Nice to have
• I would like to have our company imagery (Tamsel Energy) alongside the battery brands we offer being Borvo, KWM, Velimar and QuintaPWR
Should not have
• Unsure

```html
<!DOCTYPE html>
<html lang="en">
<head>
<meta charset="utf-8">
<title>Tamsel Energy – National Cell Storage Grant</title>
<link href="https://fonts.googleapis.com/css2?family=Albert+Sans:wght@400;500;600&family=Figtree:wght@400;500&display=swap" rel="stylesheet">
<style>
  :root {
    --navy: #2d3447;
    --red: #c1272d;
    --body: #4b5162;
    --white: #ffffff;
    --ink: #1a1212;
    --dash: #3a4152;
    --bulb: #f5d24a;
    --bulb-base: #b9bcc4;
  }
  * { margin: 0; padding: 0; box-sizing: border-box; }
  html, body { width: 1200px; height: 3955px; overflow: hidden; background: var(--white); }
  body { position: relative; font-family: "Albert Sans", sans-serif; color: var(--body); }

  .header { position: absolute; left: 0; top: 0; width: 1200px; height: 189px; background: var(--navy); }
  .brand { position: absolute; left: 72px; top: 52px; display: flex; align-items: center; gap: 18px; }
  .brand-square { width: 84px; height: 84px; background: var(--white); }
  .brand-name { font-family: "Albert Sans", sans-serif; font-weight: 600; font-size: 50px; line-height: 84px; letter-spacing: 1px; color: var(--white); }

  .greeting { position: absolute; left: 71px; top: 306px; font-size: 58px; font-weight: 500; color: var(--red); letter-spacing: -0.5px; }

  .intro { position: absolute; left: 71px; top: 422px; width: 1100px; }
  .intro p { font-size: 38px; line-height: 63.5px; letter-spacing: -0.6px; margin-bottom: 64px; white-space: nowrap; }

  .notice { position: absolute; left: 71px; top: 1254px; width: 1058px; height: 271px; background: var(--navy); border-radius: 18px; padding: 38px 40px 0 29px; color: var(--white); font-family: "Figtree", sans-serif; font-size: 35px; line-height: 57px; white-space: nowrap; }
  .notice .bulb { display: inline-block; width: 22px; height: 30px; vertical-align: -2px; margin-right: 8px; }

  .divider { position: absolute; left: 41px; top: 1636px; width: 1121px; height: 0; border-top: 2px dashed var(--dash); }

  .benefits-title { position: absolute; left: 71px; top: 1752px; font-size: 58px; line-height: 70px; font-weight: 500; color: var(--navy); letter-spacing: -0.8px; white-space: nowrap; }

  .benefits { position: absolute; left: 75px; top: 1977px; list-style: none; }
  .benefits li { position: relative; padding-left: 86px; font-size: 38px; line-height: 63.5px; letter-spacing: -0.6px; white-space: nowrap; margin-bottom: 42px; }
  .benefits li:last-child { margin-bottom: 0; }
  .benefits li svg { position: absolute; left: 0; top: 5px; width: 52px; height: 52px; }

  .hero { position: absolute; left: 0; top: 2874px; width: 1200px; height: 1081px;
    background: linear-gradient(180deg, #284a80 0%, #5f86b6 30%, #a8bfd6 52%, #6f8fb8 72%, #2f5590 100%); }
  .cta-card { position: absolute; left: 71px; top: 3064px; width: 1058px; height: 697px; background: var(--white); border-radius: 30px; padding: 50px 35px 0 35px; }
  .cta-title { font-size: 77px; line-height: 92px; font-weight: 500; color: var(--ink); letter-spacing: -0.5px; font-family: "Figtree", sans-serif; white-space: nowrap; }
  .cta-text { margin-top: 34px; font-size: 40px; line-height: 63px; color: var(--ink); letter-spacing: -0.5px; white-space: nowrap; }
  .cta-actions { position: absolute; left: 35px; top: 551px; display: flex; gap: 29px; }
  .btn { height: 91px; border-radius: 9px; display: flex; align-items: center; gap: 16px; padding: 0 28px; font-size: 31px; font-weight: 500; white-space: nowrap; }
  .btn svg { width: 36px; height: 36px; }
  .btn-call { width: 218px; background: var(--red); color: var(--white); }
  .btn-reply { width: 281px; border: 2px solid var(--red); color: var(--red); }
</style>
</head>
<body>
  <header class="header">
    <div class="brand">
      <div class="brand-square"></div>
      <span class="brand-name">TAMSEL ENERGY</span>
    </div>
  </header>

  <h1 class="greeting">Hi [First Name],</h1>

  <section class="intro">
    <p>Great news! With the federal election now decided, the<br>National Household Cell Grant Initiative is<br>officially on the way.</p>
    <p>While the scheme hasn’t formally launched yet, it’s<br>guaranteed—and like the solar rebate before it, the subsidy<br>reduces each year, so the earlier you install, the more you’ll<br>save.</p>
    <p>Crucially, the subsidy is only available once per household, so<br>it makes sense to install a system that fully meets your home’s<br>battery needs right from the start.</p>
  </section>

  <aside class="notice">
    <svg class="bulb" viewBox="0 0 22 30"><circle cx="11" cy="10" r="9" fill="var(--bulb)"/><rect x="7" y="18" width="8" height="8" rx="2" fill="var(--bulb-base)"/></svg>Important: The subsidy is limited to one per household, so<br>it’s smart to install a battery system that meets your full<br>energy needs now.
  </aside>

  <div class="divider"></div>

  <h2 class="benefits-title">Why add a battery to your existing<br>solar system now?</h2>

  <ul class="benefits">
    <li><svg viewBox="0 0 52 52"><circle cx="26" cy="26" r="26" fill="#c1272d"/><path d="M15 27l8 8 15-16" fill="none" stroke="#fff" stroke-width="5" stroke-linecap="round" stroke-linejoin="round"/></svg>Store your excess solar energy instead of sending it<br>back to the grid for low feed-in tariffs</li>
    <li><svg viewBox="0 0 52 52"><circle cx="26" cy="26" r="26" fill="#c1272d"/><path d="M15 27l8 8 15-16" fill="none" stroke="#fff" stroke-width="5" stroke-linecap="round" stroke-linejoin="round"/></svg>Use your stored solar power at night, when electricity<br>prices are highest (typically 5–8pm)</li>
    <li><svg viewBox="0 0 52 52"><circle cx="26" cy="26" r="26" fill="#c1272d"/><path d="M15 27l8 8 15-16" fill="none" stroke="#fff" stroke-width="5" stroke-linecap="round" stroke-linejoin="round"/></svg>Slash your power bills and avoid rising time-of-<br>use charges</li>
    <li><svg viewBox="0 0 52 52"><circle cx="26" cy="26" r="26" fill="#c1272d"/><path d="M15 27l8 8 15-16" fill="none" stroke="#fff" stroke-width="5" stroke-linecap="round" stroke-linejoin="round"/></svg>Protect your home from power outages</li>
    <li><svg viewBox="0 0 52 52"><circle cx="26" cy="26" r="26" fill="#c1272d"/><path d="M15 27l8 8 15-16" fill="none" stroke="#fff" stroke-width="5" stroke-linecap="round" stroke-linejoin="round"/></svg>Increase your self-sufficiency and long-<br>term energy security</li>
  </ul>

  <section class="hero" role="img" aria-label="Rooftop solar panels under a blue sky with clouds"></section>

  <div class="cta-card">
    <h2 class="cta-title">Federal Battery Subsidy<br>Confirmed – Act Early,<br>Save More</h2>
    <p class="cta-text">Claim your one-time Federal Battery Subsidy and<br>save thousands—before the rebate winds down.</p>
    <div class="cta-actions">
      <span class="btn btn-call">Call Us
        <svg viewBox="0 0 24 24" fill="none" stroke="#fff" stroke-width="1.6" stroke-linecap="round" stroke-linejoin="round"><path d="M5 3h4l2 5-2.5 1.5a11 11 0 0 0 6 6L16 13l5 2v4a2 2 0 0 1-2 2A16 16 0 0 1 3 5a2 2 0 0 1 2-2z"/><path d="M15 3a6 6 0 0 1 6 6M15 7a2 2 0 0 1 2 2"/></svg>
      </span>
      <span class="btn btn-reply">Reply to Us
        <svg viewBox="0 0 24 24" fill="none" stroke="#c1272d" stroke-width="1.6" stroke-linecap="round" stroke-linejoin="round"><path d="M9 6L4 11l5 5"/><path d="M4 11h10a6 6 0 0 1 6 6v1"/></svg>
      </span>
    </div>
  </div>
</body>
</html>
```